Financial firm simple design

Classic business card design for a financial fund. 2 sided card- white on both sides.. One with just the company name centered and the other w the info. info included on that is :

Name
Company position
phone number
fax
email
website

Industry/Entity Type

Financial

```html
<!DOCTYPE html>
<html lang="en">
<head>
<meta charset="utf-8">
<title>Norvale Investments — Business Card</title>
<link rel="stylesheet" href="https://fonts.googleapis.com/css2?family=Cinzel:wght@400&family=Questrial&family=Montserrat:wght@700&display=swap">
<style>
  :root {
    --page-bg: #e9e9ee;
    --card-bg: #ffffff;
    --navy: #1f3f73;
    --ink: #1b1b1f;
    --muted: #4a4a52;
    --rule: #b9b9c2;
    --shadow: rgba(40, 40, 60, 0.12);
  }
  * { box-sizing: border-box; margin: 0; padding: 0; }
  html, body {
    width: 1200px; height: 934px; overflow: hidden;
    background: var(--page-bg);
  }
  .sheet {
    width: 1200px; height: 934px;
    display: flex; flex-direction: column;
    align-items: center; justify-content: center; gap: 40px;
  }
  .card {
    position: relative;
    width: 720px; height: 412px;
    background: var(--card-bg);
    box-shadow: 0 6px 18px var(--shadow);
  }
  .wordmark {
    font-family: "Cinzel", "Times New Roman", serif;
    font-weight: 400;
    color: var(--navy);
    letter-spacing: 0.06em;
    white-space: nowrap;
  }
  .card--front {
    display: flex; align-items: center; justify-content: center;
  }
  .card--front .wordmark { font-size: 34px; }
  .card--back .wordmark {
    position: absolute; right: 56px; top: 64px; font-size: 30px;
  }
  .contact-row {
    position: absolute; left: 48px; right: 48px; bottom: 58px;
    display: flex; align-items: center; gap: 26px;
    font-family: "Questrial", "Century Gothic", sans-serif;
  }
  .person { flex: 0 0 auto; }
  .person__name {
    font-family: "Montserrat", "Century Gothic", sans-serif;
    font-weight: 700; font-size: 17px; letter-spacing: 0.05em;
    color: var(--ink);
  }
  .person__title { font-size: 15px; color: var(--muted); margin-top: 2px; }
  .divider { width: 1px; height: 38px; background: var(--rule); flex: 0 0 auto; }
  .details { display: flex; flex-direction: column; gap: 6px; font-size: 14px; color: var(--ink); }
  .details__item { display: flex; align-items: center; gap: 8px; white-space: nowrap; }
  .icon { width: 15px; height: 15px; flex: 0 0 auto; }
</style>
</head>
<body>
<main class="sheet">
  <section class="card card--front" aria-label="Card front">
    <span class="wordmark">Norvale Investments</span>
  </section>

  <section class="card card--back" aria-label="Card back">
    <span class="wordmark">Norvale Investments</span>

    <div class="contact-row">
      <div class="person">
        <div class="person__name">DANIEL HARTWELL</div>
        <div class="person__title">General Manager</div>
      </div>

      <span class="divider"></span>

      <div class="details">
        <div class="details__item">
          <svg class="icon" viewBox="0 0 16 16" aria-hidden="true">
            <circle cx="8" cy="8" r="7.2" fill="none" stroke="var(--navy)" stroke-width="1.2"/>
            <path d="M5.4 4.3l1.3-.3.7 1.8-.9.7a5 5 0 0 0 2.3 2.3l.7-.9 1.8.7-.3 1.3c-3 .4-6-2.6-5.6-5.6z" fill="var(--navy)"/>
          </svg>
          <span>(555) 014-2287</span>
        </div>
        <div class="details__item">
          <svg class="icon" viewBox="0 0 16 16" aria-hidden="true">
            <circle cx="8" cy="8" r="8" fill="var(--navy)"/>
            <rect x="5.5" y="4" width="5" height="3" fill="#fff"/>
            <rect x="4" y="7" width="8" height="3.5" rx="0.6" fill="#fff"/>
            <rect x="5.5" y="9.5" width="5" height="2.5" fill="#fff" stroke="var(--navy)" stroke-width="0.6"/>
          </svg>
          <span>(555) 014-2291</span>
        </div>
      </div>

      <span class="divider"></span>

      <div class="details">
        <div class="details__item">
          <svg class="icon" viewBox="0 0 16 16" aria-hidden="true">
            <circle cx="8" cy="8" r="8" fill="var(--navy)"/>
            <rect x="4" y="5.2" width="8" height="5.6" fill="#fff"/>
            <path d="M4 5.2l4 3 4-3" fill="none" stroke="var(--navy)" stroke-width="0.8"/>
          </svg>
          <span>info@norvaleinvest.com</span>
        </div>
        <div class="details__item">
          <svg class="icon" viewBox="0 0 16 16" aria-hidden="true">
            <circle cx="8" cy="8" r="8" fill="var(--navy)"/>
            <g fill="none" stroke="#fff" stroke-width="0.8">
              <circle cx="8" cy="8" r="4.6"/>
              <ellipse cx="8" cy="8" rx="2" ry="4.6"/>
              <path d="M3.4 8h9.2M4 5.8h8M4 10.2h8"/>
            </g>
          </svg>
          <span>www.norvaleinvest.com</span>
        </div>
      </div>
    </div>
  </section>
</main>
</body>
</html>
```